Inspirational quotes poster shop seeks poster designs

Hi! We are launching an eshop with design posterss featuring inspirational quotes. We need a first poster design while looking for further cooperation on around 20 poster designs. We need outputs in the format that can go to high quality print (size at least 100x70cm).

For the first design feel free to choose any of the following quotes to depict:

1. "Stop starting. Start finishing." Author: Torvald Essunger, Klangora
2. "A problem well stated is a problem half solved." Author: Walter P. Brimsley, American inventor
3. "The best way to predict the future is to invent it." Author: Dale Hubbs, Quince

Designs should be rarther simple, think please of your whole concept and how various posters would go together. Every poster can be quite different though, in terms of fonts, colours and overall design, together they should however form and interesting collage.

Designs must contain the quote, author & company. it can be pure text or some indication of the sense of the quote.

Design must also feature company name/logo (not available yet, for now please use "thoughtvolta" as a working name), QR code with a title "Read the story"

See these posters for design we like (for inspiration ONLY!):
http://www.launchtonics.example/products/launch-print-its-simple-until-you-make-it-complicated
http://www.launchtonics.example/products/launch-print-marcus-feldane-less-meetings-more-doing
http://www.launchtonics.example/products/launch-print-gordon-ashfeld-stop-sketching-start-building

Hi to everybody! Sorry for the spam, some of you have been struggling with finding the crux in the quote, so here I offer some ideas what to look for in them. It's up to you to take it, leave it or change it:)

Stop starting, start finishing -
1 - stop starting with many times repeated small word starting, perhaps large word starting made of small words starting, with it contrasting start finishing in normal bold font.
2 - STARTING could look quite unfinished, sketchy, especially -ING could look more unfinished then the rest , e.g. just rough indication of outline of the letters, again contrasting with start finishing will clean & neat writting.

Problem well stated is a problem half solved - look for something that is clearer by defining the problem. Perhaps in a simple sketch like here http://www.launchtonics.example/products/launch-print-its-simple-until-you-make-it-complicated  point out a route from a problem (light = flame), to a solution (lightbulb, lightbulb design drawing or something like that).

Anyway, despite preference for simple design, I am still looking for some smart, creative, catchy idea in the design. Check with yourself if it's something you can would want to buy and hang up on your wall.

Good luck to all of you and again, thank you all very much for participation!
Radim

Target Market(s)

businesses of every size, from startups to large corporates seeking culture change or motivation kick up

Industry/Entity Type

Shop

Requirements
Must have
• I strongly prefer portrait orientation of the poster!

Nice to have
• Quotes themselves are often on the edge, teasing, so the design can be.
Should not have
• Try to avoid traditional dialoge bubble for the quote itself as the first obvious idea for depicting a quote.

Avoid using photos (not simple then) or too many colours.

Of course, by no means use a COPY of existing designs I linked to for inspiration. It just shows what we like.

```html
<!DOCTYPE html>
<html lang="en">
<head>
<meta charset="utf-8">
<title>The Best Way to Predict the Future — Poster</title>
<link rel="stylesheet" href="https://fonts.googleapis.com/css2?family=Source+Sans+3:wght@400;600;700&display=swap">
<style>
  :root {
    --poster-pink: #c4316a;
    --quote-maroon: #7a0008;
    --highlight-white: #ffffff;
    --brand-tone: #8f1f4f;
    --ink-black: #111111;
  }
  html, body {
    margin: 0;
    padding: 0;
    overflow: hidden;
  }
  .poster {
    position: relative;
    width: 840px;
    height: 1200px;
    background: var(--poster-pink);
    overflow: hidden;
    font-family: "Source Sans 3", "Myriad Pro", sans-serif;
  }
  .brand-name {
    position: absolute;
    top: 60px;
    left: 0;
    width: 100%;
    text-align: center;
    font-size: 22px;
    font-weight: 600;
    letter-spacing: 0.02em;
    text-transform: uppercase;
    color: var(--brand-tone);
  }
  .quote {
    position: absolute;
    inset: 0;
    width: 840px;
    height: 1200px;
  }
  .quote-line {
    font-family: "Source Sans 3", "Myriad Pro", sans-serif;
    font-weight: 700;
    fill: var(--quote-maroon);
  }
  .quote-line--highlight {
    fill: var(--highlight-white);
  }
  .strike-rule {
    fill: var(--highlight-white);
  }
  .attribution {
    position: absolute;
    left: 372px;
    top: 993px;
    width: 346px;
    margin: 0;
    border-top: 1.5px solid var(--ink-black);
    padding-top: 6px;
    text-align: center;
    font-size: 23px;
    color: var(--ink-black);
  }
  .attribution-author {
    font-weight: 700;
  }
  .story-link {
    position: absolute;
    left: 34px;
    top: 968px;
    width: 110px;
    text-align: center;
  }
  .story-link-title {
    margin: 0 0 8px;
    font-size: 15px;
    font-weight: 600;
    color: var(--quote-maroon);
    text-transform: uppercase;
    letter-spacing: 0.04em;
  }
  .story-code {
    display: block;
    width: 110px;
    height: 110px;
  }
  .story-code-frame {
    fill: none;
    stroke: var(--quote-maroon);
    stroke-width: 3;
  }
  .story-code-fill {
    fill: var(--quote-maroon);
    opacity: 0.25;
  }
</style>
</head>
<body>
  <main class="poster">
    <div class="brand-name">thoughtvolta</div>

    <svg class="quote" viewBox="0 0 840 1200" aria-label="The best way to predict the future is to invent it.">
      <text class="quote-line" x="28" y="404" font-size="118" textLength="700" lengthAdjust="spacingAndGlyphs">THE BEST WAY</text>
      <text class="quote-line" x="34" y="494" font-size="109" textLength="554" lengthAdjust="spacingAndGlyphs">TO FUTURE</text>
      <rect class="strike-rule" x="10" y="450" width="616" height="4"/>
      <text class="quote-line" x="34" y="583" font-size="112" textLength="570" lengthAdjust="spacingAndGlyphs">TO PREDICT</text>
      <text class="quote-line quote-line--highlight" x="26" y="693" font-size="133" textLength="780" lengthAdjust="spacingAndGlyphs">THE FUTURE</text>
      <text class="quote-line" x="34" y="791" font-size="116" textLength="782" lengthAdjust="spacingAndGlyphs">IS TO INVENT IT.</text>
    </svg>

    <div class="story-link">
      <p class="story-link-title">Read the story</p>
      <svg class="story-code" viewBox="0 0 110 110" role="img" aria-label="QR code linking to the story behind the quote">
        <rect class="story-code-fill" x="4" y="4" width="102" height="102"/>
        <rect class="story-code-frame" x="1.5" y="1.5" width="107" height="107"/>
      </svg>
    </div>

    <p class="attribution"><span class="attribution-author">Dale Hubbs,</span> Quince</p>
  </main>
</body>
</html>
```